Mindarrowco, inc
Transform your mind and your body will follow...
Mindarrowco, inc - Health
Health
www.velanix.com
We are an online health and wellness company that sells four programs. BodyTrim (weightloss), AirClear (stop smoking), CalmSips (alcohol management), and SoftMind (Stress Management).
We like websites that lists our products on the left-hand side of the page vertically. Have large graphic images. Several CTA buttons throughout. A site that portrays beautty and motivation, an overall "fitness/health" approach. Very clean and simple designs work best.
White
Dark red
left side
http://www.velanix.com/velanix-ology/
http://www.velanix.com/products/velanix-berrytrim/
We enjoy having the large image in the background with transparent copy/content over it. Please create a website that copies www.velanix.com but please add your own creative touches.

```html
<!DOCTYPE html>
<html lang="en">
<head>
<meta charset="utf-8">
<title>Mindarrowco, inc – Transform your mind and your body will follow</title>
<link rel="stylesheet" href="https://fonts.googleapis.com/css2?family=Arimo:wght@400;700&family=Lora:wght@400;700&display=swap">
<style>
:root{
  --red:#a3161b;
  --red-dark:#7c0f13;
  --bar:#2b1d1d;
  --white:#ffffff;
  --text:#3a3a3a;
  --muted:#6b6b6b;
  --panel:rgba(255,255,255,0.93);
  --line:#d8d8d8;
  --sky-top:#3b4e66;
  --sky-mid:#c9b8a6;
  --sea:#55677c;
  --rock:#1e2630;
  --green:#6a9a3a;
}
*{box-sizing:border-box;margin:0;padding:0}
html,body{width:1200px;height:952px;overflow:hidden}
body{font-family:"Arimo",Arial,sans-serif;color:var(--text);font-size:11px;line-height:1.45}
.page{position:relative;width:1200px;height:952px;overflow:hidden}
.backdrop{position:absolute;inset:0;background:
  radial-gradient(ellipse at 55% 38%,#f3e6cf 0%,rgba(243,230,207,0) 40%),
  linear-gradient(180deg,var(--sky-top) 0%,#7f8ea0 25%,var(--sky-mid) 45%,#8e9aa8 58%,var(--sea) 72%,var(--rock) 100%)}
.topbar{position:absolute;left:0;top:0;width:1200px;height:22px;background:var(--bar)}
.mainnav{position:absolute;left:258px;top:0;display:flex;gap:22px;height:22px;align-items:center}
.mainnav a{color:var(--white);text-decoration:none;font-size:10px;font-weight:700;letter-spacing:.3px}
.join{position:absolute;left:870px;top:4px;color:#d9c9c9;font-size:9px;font-weight:700}
.brand{position:absolute;left:232px;top:52px;display:flex;align-items:center;gap:6px}
.brand-dot{width:16px;height:16px;border-radius:50%;background:var(--red)}
.brand-name{font-family:"Lora",Georgia,serif;font-weight:700;font-size:26px;color:var(--red)}
.login{position:absolute;left:438px;top:32px;width:230px;height:58px;background:var(--panel)}
.login-tab{position:absolute;left:0;top:0;width:26px;height:58px;background:var(--red);color:#fff;font-size:9px;font-weight:700;writing-mode:vertical-rl;transform:rotate(180deg);text-align:center}
.login input{position:absolute;top:8px;width:90px;height:14px;border:1px solid var(--line);font-size:8px;padding:0 3px;color:var(--muted);font-family:inherit}
.login .btn-login{position:absolute;left:32px;top:28px;background:var(--red);color:#fff;font-size:8px;padding:1px 6px;font-weight:700}
.login .links{position:absolute;left:32px;top:44px;font-size:7.5px;color:var(--muted)}
.cart{position:absolute;left:770px;top:32px;width:185px;height:58px;background:var(--panel);padding:6px 0 0 46px;font-size:7.5px;color:var(--muted);text-align:right;padding-right:62px}
.cart h4{font-size:11px;color:var(--text);font-weight:700}
.cart .count{color:var(--red)}
.cart svg{position:absolute;right:8px;top:8px}
.stage{position:absolute;left:438px;top:95px;width:517px;height:382px;background:rgba(255,255,255,0.25)}
.tabs{position:absolute;left:0;top:0;width:52px;height:382px;background:var(--white)}
.tab{height:95.5px;border-bottom:1px solid var(--line);display:flex;align-items:center;justify-content:center}
.tab span{writing-mode:vertical-rl;transform:rotate(180deg);font-family:"Lora",Georgia,serif;font-weight:700;font-size:14px;color:#222}
.thumbs{position:absolute;left:57px;top:6px;width:148px}
.thumb{height:88px;margin-bottom:6px;border:2px solid #fff}
.t1{background:linear-gradient(135deg,#5aa0c4,#a9d3c9)}
.t2{background:linear-gradient(135deg,#1c7fb0,#73c1d8)}
.t3{background:linear-gradient(135deg,#7a4a5c,#c98a78)}
.t4{background:linear-gradient(135deg,#e8a95a,#5b6f8a)}
.hero{position:absolute;left:210px;top:6px;width:301px;height:370px;background:linear-gradient(170deg,#7fb6d8 0%,#a9cde0 45%,#6c9a50 75%,#4f7a34 100%)}
.hero-caption{position:absolute;left:8px;right:8px;bottom:10px;background:rgba(255,255,255,0.85);padding:6px 8px;font-size:8px;color:var(--text)}
.more{color:var(--red);font-weight:700}
.intro{position:absolute;left:438px;top:477px;width:517px;height:218px;background:var(--panel);padding:14px 14px}
.intro h2{font-family:"Lora",Georgia,serif;font-size:19px;color:var(--red);font-weight:700;margin-bottom:6px}
.intro p{font-size:9px;color:var(--muted);line-height:1.5}
.newsletter{position:absolute;left:438px;top:697px;width:162px;height:211px;background:var(--panel)}
.newsletter h3{background:var(--bar);color:#fff;font-size:10px;font-weight:700;padding:6px 8px;line-height:1.25}
.newsletter label{display:block;margin:9px 8px 0;border:1px solid var(--line);background:#fff;font-size:8px;padding:2px 4px;color:var(--muted)}
.newsletter .btn{display:inline-block;margin:9px 8px;background:var(--red);color:#fff;font-size:8px;font-weight:700;padding:2px 7px}
.feed-band{position:absolute;left:600px;top:697px;width:38px;height:211px;background:var(--red);display:flex;align-items:center;justify-content:center}
.feed-band span{writing-mode:vertical-rl;transform:rotate(180deg);color:#fff;font-weight:700;font-size:11px;letter-spacing:.5px}
.feed{position:absolute;left:638px;top:697px;width:317px;height:211px;background:var(--panel);padding:8px 8px}
.post{position:relative;height:98px;padding-left:96px}
.post + .post{border-top:1px solid var(--line);padding-top:6px}
.post-photo{position:absolute;left:0;top:2px;width:88px;height:82px}
.post + .post .post-photo{top:8px}
.p1{background:linear-gradient(160deg,#9cc3d6,#5d8a42)}
.p2{background:linear-gradient(160deg,#b7cfdc,#4d7b3a)}
.post h5{font-family:"Lora",Georgia,serif;font-size:11px;color:#222}
.post p{font-size:7.5px;color:var(--muted);line-height:1.4}
.post-actions{position:absolute;right:0;bottom:6px;display:flex;gap:3px}
.post-actions i{display:block;width:26px;height:9px;background:var(--green)}
.post-actions i + i{background:#6f8fc2}
.footer{position:absolute;left:0;top:908px;width:1200px;height:44px;background:var(--bar);color:#d9c9c9;font-size:9px}
.footer .links{position:absolute;left:255px;top:14px}
.footer .copy{position:absolute;left:525px;top:14px}
.cards{position:absolute;left:800px;top:10px;display:flex;gap:5px}
.cards i{display:block;width:34px;height:22px;background:#e9e9e9;border-radius:2px}
</style>
</head>
<body>
<div class="page">
  <div class="backdrop" role="img" aria-label="Full page photograph of a calm sea at sunrise with dark rocks in the foreground"></div>

  <header class="topbar">
    <nav class="mainnav">
      <a href="#">HOME</a><a href="#">COMPANY</a><a href="#">ORDER PRODUCTS</a><a href="#">LIFESTYLE</a><a href="#">CONTACT</a>
    </nav>
    <div class="join">JOIN US</div>
  </header>

  <div class="brand"><span class="brand-dot"></span><span class="brand-name">mindarrowco</span></div>

  <form class="login">
    <div class="login-tab">LOGIN</div>
    <input style="left:32px" value="User Name" readonly>
    <input style="left:130px" value="Password" readonly>
    <span class="btn-login">Login</span>
    <span class="links">Register Now | Forgot Password</span>
  </form>

  <div class="cart">
    <h4>My Cart</h4>
    <div>2 items in basket</div>
    <div class="count">Checkout</div>
    <div>View cart</div>
    <svg width="44" height="40" viewBox="0 0 44 40" aria-hidden="true">
      <path d="M12 14 L22 3 L32 14" fill="none" stroke="#a3161b" stroke-width="3"/>
      <path d="M3 14 H41 L36 37 H8 Z" fill="#a3161b"/>
      <path d="M14 19 V32 M22 19 V32 M30 19 V32" stroke="#fff" stroke-width="2"/>
    </svg>
  </div>

  <section class="stage">
    <nav class="tabs">
      <div class="tab"><span>BodyTrim</span></div>
      <div class="tab"><span>AirClear</span></div>
      <div class="tab"><span>CalmSips</span></div>
      <div class="tab"><span>SoftMind</span></div>
    </nav>
    <div class="thumbs">
      <div class="thumb t1" role="img" aria-label="Photo of a smiling woman outdoors"></div>
      <div class="thumb t2" role="img" aria-label="Photo of a pool with the word no spelled out"></div>
      <div class="thumb t3" role="img" aria-label="Photo of friends sharing a drink"></div>
      <div class="thumb t4" role="img" aria-label="Photo of a person relaxing at sunset"></div>
    </div>
    <div class="hero" role="img" aria-label="Large photo of a fit woman stretching on grass under a blue sky">
      <div class="hero-caption">Start each day with a clear goal and a calm mind. Our guided program helps you build small habits that last, eat with care, move more and feel stronger week after week. Begin your journey today. <span class="more">Read more</span></div>
    </div>
  </section>

  <section class="intro">
    <h2>Mindarrowco</h2>
    <p>We believe lasting change starts in the mind. Our online programs guide you step by step, helping you understand your habits and replace them with healthier choices. Whether you want to lose weight, quit smoking, drink less or simply feel less stressed, each program offers short daily lessons, simple tools and steady support. Thousands of members have already found a lighter, calmer and more confident way of living. You can learn at your own pace, from any device, whenever it suits you. Our team of coaches and health experts keeps every lesson clear, practical and kind. Transform your mind and your body will follow. Join today and take the first step toward a healthier you with a plan made for real life.</p>
  </section>

  <form class="newsletter">
    <h3>GET MINDARROWCO NEWSLETTER</h3>
    <label>Name</label>
    <label>Email ID</label>
    <span class="btn">Subscribe</span>
  </form>

  <div class="feed-band"><span>HEALTHY NEWS FEED</span></div>

  <section class="feed">
    <article class="post">
      <div class="post-photo p1" role="img" aria-label="Photo of a man running outdoors"></div>
      <h5>Meet Callum</h5>
      <p>Callum lost twenty pounds in three months by changing how he thinks about food. He now walks every morning, cooks fresh meals at home and sleeps better than ever before. Read how small steps made a big difference.</p>
      <span class="more" style="font-size:8px">Read more</span>
      <div class="post-actions"><i></i><i></i></div>
    </article>
    <article class="post">
      <div class="post-photo p2" role="img" aria-label="Photo of a man training in a park"></div>
      <h5>Meet Callum</h5>
      <p>After years of stress at work, Callum found calm through short daily lessons. He learned simple breathing tools, set clear limits and made time for exercise. Today he feels focused, rested and ready for each new day.</p>
      <span class="more" style="font-size:8px">Read more</span>
      <div class="post-actions"><i></i><i></i></div>
    </article>
  </section>

  <footer class="footer">
    <div class="links">Home | Privacy | Support | Contact</div>
    <div class="copy">Copyright 2012, mindarrowco.com</div>
    <div class="cards"><i></i><i></i><i></i><i></i></div>
  </footer>
</div>
</body>
</html>
```